Annual review for The Birchmoor Collective

The Birchmoor Collective is a small public relations agency in London specialising in corporate and public affairs. Most of our work is international and we have a strong connection to South Africa. We would like to prepare a short annual review for 2016. The review will serve as both a review of our activities in 2016, and as a credentials document. Content then will include:
1. An introduction to the business
2. Who we are
3. Projects and clients undertaken in 2016
4. News and views
We imagine it will be used mostly as a pdf but would like it to be suitable for print. We envisage it to be about 8 pages long. The design look and feel should convey a business, while small, of stature. We shall include some of our client logos but we would welcome the use of some photography / imagery to have visual impact (although we don't have very much of our own!). The corporate look and feel is white, grey and black.

Industry/Entity Type

Public Relation

Font styles to use
Sans Serif

Requirements
Must have
• My project must convey a business with flair and gravitas, that punches above its weight.
Nice to have
• Thoughtful use of imagery.

```html
<!DOCTYPE html>
<html lang="en">
<head>
<meta charset="utf-8">
<title>The Birchmoor Collective – Annual Review 2016</title>
<link rel="stylesheet" href="https://fonts.googleapis.com/css2?family=Montserrat:wght@700&family=Roboto+Condensed:wght@400;700&family=Lato:wght@400&display=swap">
<style>
  :root {
    --ink: #111111;
    --slate: #4f5157;
    --slate-dark: #55575d;
    --slate-mid: #7b7e84;
    --paper: #ffffff;
    --backdrop: #ffffff;
    --text-light: #f2f2f2;
  }
  html, body {
    margin: 0;
    padding: 0;
    width: 1200px;
    height: 899px;
    overflow: hidden;
    background: var(--backdrop);
  }
  .spread {
    position: relative;
    width: 1200px;
    height: 899px;
  }
  .page {
    position: absolute;
    top: 108px;
    width: 517px;
    height: 664px;
    overflow: hidden;
    box-shadow: 0 4px 14px rgba(0,0,0,0.28);
  }
  /* Front cover */
  .cover {
    left: 62px;
    background: var(--paper);
  }
  .brand {
    position: absolute;
    left: 0;
    right: 0;
    display: flex;
    align-items: center;
    justify-content: center;
    gap: 12px;
    font-family: "Montserrat", sans-serif;
    font-weight: 700;
    white-space: nowrap;
  }
  .brand-dot {
    border-radius: 50%;
    border: 2px solid currentColor;
    box-sizing: border-box;
  }
  .cover .brand {
    top: 48px;
    font-size: 25px;
    color: var(--slate);
  }
  .cover .brand-dot { width: 34px; height: 34px; }
  .cover-art {
    position: absolute;
    left: 0;
    top: 0;
  }
  .title {
    position: absolute;
    left: 0;
    right: 0;
    text-align: center;
    font-family: "Roboto Condensed", sans-serif;
    line-height: 1;
  }
  .title-top {
    top: 488px;
    font-size: 54px;
    font-weight: 700;
    color: var(--slate);
    letter-spacing: -0.5px;
  }
  .title-year {
    top: 540px;
    font-size: 90px;
    font-weight: 400;
    color: var(--ink);
    letter-spacing: -1px;
  }
  .cover-url {
    position: absolute;
    left: 0;
    right: 0;
    top: 628px;
    text-align: center;
    font-family: "Lato", sans-serif;
    font-size: 14px;
    letter-spacing: 4.2px;
    color: var(--ink);
  }
  /* Back cover */
  .back {
    left: 631px;
    background: var(--slate-dark);
  }
  .back-photo {
    position: absolute;
    left: 0;
    top: 0;
    width: 100%;
    height: 300px;
    background: linear-gradient(180deg, #9a9da2 0%, #84878c 40%, #6a6d72 70%, var(--slate-dark) 100%);
  }
  .back .brand {
    top: 328px;
    font-size: 29px;
    color: var(--paper);
  }
  .back .brand-dot { width: 36px; height: 36px; }
  .contact-intro {
    position: absolute;
    left: 28px;
    right: 28px;
    top: 392px;
    text-align: center;
    font-family: "Lato", sans-serif;
    font-size: 9.4px;
    line-height: 15px;
    color: var(--text-light);
  }
  .office {
    position: absolute;
    top: 451px;
    font-family: "Lato", sans-serif;
    font-size: 9.4px;
    line-height: 17px;
    color: var(--text-light);
  }
  .office-name {
    font-family: "Roboto Condensed", sans-serif;
    font-weight: 700;
    font-size: 10.5px;
  }
  .office-london { left: 86px; }
  .office-paris { left: 319px; top: 450px; }
  .office-divider {
    position: absolute;
    left: 256px;
    top: 446px;
    width: 1px;
    height: 72px;
    background: linear-gradient(180deg, transparent, #8b8e93 30%, #8b8e93 70%, transparent);
  }
  .email {
    position: absolute;
    left: 0;
    right: 0;
    top: 542px;
    text-align: center;
    font-family: "Lato", sans-serif;
    font-size: 13.5px;
    color: var(--paper);
  }
  .email-label {
    font-family: "Roboto Condensed", sans-serif;
    font-weight: 700;
  }
  .back-band {
    position: absolute;
    left: 0;
    right: 0;
    top: 606px;
    height: 23px;
    background: var(--paper);
    text-align: center;
    font-family: "Lato", sans-serif;
    font-size: 14.5px;
    line-height: 23px;
    letter-spacing: 4.4px;
    color: var(--ink);
  }
</style>
</head>
<body>
<div class="spread">

  <section class="page cover">
    <div class="brand"><span class="brand-dot"></span>The Birchmoor Collective</div>

    <svg class="cover-art" width="517" height="664" viewBox="0 0 517 664">
      <defs>
        <linearGradient id="teamTone" x1="0" y1="0" x2="1" y2="1">
          <stop offset="0" stop-color="#d9d6d2"/>
          <stop offset="0.45" stop-color="#c8b9a8"/>
          <stop offset="0.75" stop-color="#8aa3bd"/>
          <stop offset="1" stop-color="#a47a58"/>
        </linearGradient>
      </defs>
      <!-- upper grey swoop -->
      <path d="M0 84 Q258 160 517 84 L517 112 Q258 175 0 112 Z" fill="#55575d"/>
      <path d="M0 112 Q258 175 0 112 Z" fill="#000"/>
      <path d="M0 116 Q258 176 517 116 L517 124 Q258 182 0 124 Z" fill="#0d0d0d"/>
      <!-- photo region -->
      <path d="M0 130 Q258 188 517 130 L517 448 Q258 372 0 448 Z" fill="url(#teamTone)" role="img" aria-label="Photograph of a smiling team gathered around a laptop at an office desk"/>
      <!-- lower swoop -->
      <path d="M0 448 Q258 372 517 448 L517 456 Q258 381 0 456 Z" fill="#0d0d0d"/>
      <path d="M0 461 Q258 390 517 461 L517 490 Q258 408 0 490 Z" fill="#55575d"/>
    </svg>

    <div class="title title-top">ANNUAL REVIEW</div>
    <div class="title title-year">FOR 2016</div>
    <div class="cover-url">www.birchmoorcollective.com</div>
  </section>

  <section class="page back">
    <div class="back-photo" role="img" aria-label="Monochrome photograph of colleagues at work in a bright city-view office"></div>
    <div class="brand"><span class="brand-dot"></span>The Birchmoor Collective</div>
    <p class="contact-intro">To contact The Birchmoor Collective, please leave your details and a message below. We will get back to you as soon as we can. Alternatively you can write to us at:</p>

    <div class="office office-london">
      <div class="office-name">The Birchmoor Collective</div>
      <div>24 Halden Row</div>
      <div>London EC2A 4NP</div>
    </div>
    <div class="office-divider"></div>
    <div class="office office-paris">
      <div class="office-name">The Birchmoor Collective</div>
      <div>12 rue des Tilleuls</div>
      <div>75011 Paris</div>
    </div>

    <div class="email"><span class="email-label">Or by email:</span> info@birchmoorcollective.com</div>
    <div class="back-band">www.birchmoorcollective.com</div>
  </section>

</div>
</body>
</html>
```